Indigenous consulting group needs eye-catching illustration for major education project

Need an eye-catching illustration for major regional education project which is about parents and caregivers supporting their chidden more positively and proactively through school. The idea is that we develop their capacity and skill levels to engage and influence their children and schools with an outcome of improved grades. This means reducing truancy and school suspensions and improving attitudes and study habits. For an Indigenous group it means honouring the past but at the same time shaping the future (today's kids and tomorrow's leaders). Parents and caregivers can be a positive influence and catalyst in the education process - all the research and evidence demonstrates that. It's also about the legacy we want to leave for next generations. There is also the point that in the digital and information age poor schooling is a recipe for getting left even further behind. I was thinking maybe a board game illustration with a beginning square (start school) and working through a series of squares to an end point (complete schooling with good grades). Like a Harborlin Board.

Target Market(s)

Parents/caregivers of school-aged children, NGO community groups, educators, funding bodies

Industry/Entity Type

Education

Requirements
Must have
• Board game design and colourful. Squares to house relevant text related to schooling as per some of the key words in Task Description. Could also include text like language, literacy, numeracy; and key school subject areas. Teaching staff, school liaison and administrators could also feature. The bottom line is that evidence and research shows that parents and caregivers can be a positive influence on educational outcomes in terms of how they engage, interact and influence their children and the schools themselves.
Nice to have
• A way to depict honouring the past whilst creating the future
Should not have
• Grey, dark images

```html
<!DOCTYPE html>
<html lang="en">
<head>
<meta charset="utf-8">
<title>Stay in School Board</title>
<link href="https://fonts.googleapis.com/css2?family=Fredoka:wght@600&family=Permanent+Marker&display=swap" rel="stylesheet">
<style>
  :root {
    --page: #ffffff;
    --board: #3d4fc0;
    --track-top: #3a7fe2;
    --centre: #e0e2ec;
    --maths: #1fd38c;
    --literacy: #c81fd6;
    --start: #e8773a;
    --language: #cde04a;
    --history: #3ee80a;
    --art: #e020e6;
    --friendship: #d8a81a;
    --gym: #e04a1a;
    --learning: #36c8e2;
    --win: #a832f0;
    --label: #2aa6f2;
    --label-light: #8ee6ff;
    --label-deep: #1558c4;
    --label-top: #2e6fd8;
    --arrow: #1ea8f2;
    --title: #2f7fd6;
    --token: #c8e23a;
  }
  * { margin: 0; padding: 0; box-sizing: border-box; }
  html, body { width: 1200px; height: 800px; overflow: hidden; background: var(--page); }
  .board {
    position: relative; width: 1200px; height: 800px;
    font-family: "Fredoka", "Arial Rounded MT Bold", sans-serif; font-weight: 600;
  }
  .board-frame {
    position: absolute; left: 55px; top: 0; width: 1115px; height: 790px;
    background: var(--board); border-radius: 14px;
  }
  .tile {
    position: absolute; display: flex; align-items: center; justify-content: center;
    text-align: center; color: var(--label); font-size: 34px; line-height: 1.05;
  }
  .tile span { display: block; white-space: nowrap; }
  .tile--maths { left: 105px; top: 42px; width: 170px; height: 222px; background: var(--maths); color: var(--label-deep); }
  .tile--maths span { transform: rotate(60deg); }
  .tile--literacy { left: 95px; top: 305px; width: 180px; height: 225px; background: var(--literacy); color: var(--label-light); }
  .tile--start { left: 95px; top: 555px; width: 195px; height: 190px; background: var(--start); color: var(--label-deep); }
  .tile--start span { transform: rotate(-45deg); }
  .top-track {
    position: absolute; left: 308px; top: 20px; width: 657px; height: 135px;
    background: var(--track-top); border-radius: 12px;
  }
  .tile--language { left: 333px; top: 45px; width: 200px; height: 85px; background: var(--language); color: var(--label-top); }
  .tile--history { left: 565px; top: 45px; width: 225px; height: 92px; background: var(--history); color: var(--label-top); }
  .tile--art { left: 825px; top: 38px; width: 120px; height: 87px; background: var(--art); color: var(--label-light); }
  .tile--art span { transform: rotate(-30deg); }
  .tile--friendship { left: 988px; top: 35px; width: 135px; height: 187px; background: var(--friendship); color: var(--label-deep); }
  .tile--friendship span { transform: rotate(70deg); }
  .tile--gym { left: 1010px; top: 262px; width: 110px; height: 195px; background: var(--gym); color: var(--label-light); }
  .tile--gym span { transform: rotate(70deg); }
  .tile--learning { left: 1005px; top: 492px; width: 128px; height: 163px; background: var(--learning); color: var(--label-deep); }
  .tile--learning span { transform: rotate(60deg); }
  .tile--win { left: 988px; top: 682px; width: 148px; height: 80px; background: var(--win); color: var(--label-light); font-size: 30px; }
  .centre-panel {
    position: absolute; left: 312px; top: 160px; width: 648px; height: 605px;
    background: var(--centre);
  }
  .centre-title {
    position: absolute; inset: 0;
    font-family: "Permanent Marker", "Comic Sans MS", cursive;
    font-weight: 400; color: var(--title); text-transform: none;
  }
  .centre-title span { position: absolute; display: block; line-height: 1; white-space: nowrap; }
  .title-stay { left: 40px; top: 10px; font-size: 200px; letter-spacing: 6px; }
  .title-in { left: 150px; top: 205px; font-size: 190px; letter-spacing: 14px; }
  .title-school { left: 18px; top: 385px; font-size: 190px; letter-spacing: 2px; }
  .token {
    position: absolute; left: 805px; top: 415px; width: 100px; height: 100px;
    border-radius: 50%; background: var(--token);
  }
  .arrow { position: absolute; }
</style>
</head>
<body>
<main class="board">
  <div class="board-frame"></div>

  <div class="tile tile--maths"><span>Mathematics</span></div>
  <div class="tile tile--literacy"><span>Literacy</span></div>
  <div class="tile tile--start"><span>Start School</span></div>

  <div class="top-track"></div>
  <div class="tile tile--language"><span>Language</span></div>
  <div class="tile tile--history"><span>History</span></div>
  <div class="tile tile--art"><span>Art</span></div>

  <div class="tile tile--friendship"><span>Friendship</span></div>
  <div class="tile tile--gym"><span>Gym</span></div>
  <div class="tile tile--learning"><span>Learning</span></div>
  <div class="tile tile--win"><span>All A's<br>You Win</span></div>

  <section class="centre-panel">
    <h1 class="centre-title">
      <span class="title-stay">STAY</span>
      <span class="title-in">IN</span>
      <span class="title-school">School</span>
    </h1>
  </section>
  <div class="token" role="img" aria-label="Small cheerful game token character"></div>

  <svg class="arrow arrow--up" style="left:55px;top:460px" width="88" height="180" viewBox="0 0 88 180">
    <polygon points="44,0 88,55 62,55 62,180 26,180 26,55 0,55" fill="var(--arrow)"/>
  </svg>
  <svg class="arrow arrow--right" style="left:592px;top:10px" width="85" height="24" viewBox="0 0 85 24">
    <polygon points="0,8 60,8 60,0 85,12 60,24 60,16 0,16" fill="var(--arrow)"/>
  </svg>
  <svg class="arrow arrow--down" style="left:925px;top:312px" width="88" height="185" viewBox="0 0 88 185">
    <polygon points="28,0 60,0 60,125 88,125 44,185 0,125 28,125" fill="var(--arrow)"/>
  </svg>
</main>
</body>
</html>
```